Fahrzeugbeschriftung eines Varlenne Kadro Kastenwagens L3H2 für die Veranstaltungsbranche
Zielgruppe
Ich bin ein Einzelunternehmer in der Eventbranche (Fachkraft für Veranstaltungstechnik), speziell der technische Dienstleister für Beschallung (Tontechnik), Beleuchtung (Lichttechnik), Video- und Präsentationstechnik (Beamer, Videoscreens, etc), Bühnenbau, Touring- und Messeservice. Meine Kunden schätzen an mir, dass ich auf Wünsche direkt eingehe und schnell darauf reagieren kann. Zielgruppe sind sowohl kleine Feiern, als auch größere Konzerte und Produktpräsentationen, sowie Tagungen. Von Rock'n'Roll bis Gala ist alles vertreten.
Aufgabenstellung
Beschriftet wird ein Varlenne Kadro L3H2 mit Baujahr 2019 in der Farbe Reinweiß.
Eindeutig und einprägsam, jedoch nicht zu Aufdringlich. Das plumpe Auftreten eines Handwerkers sollte nicht vermittelt werden, jedoch auch nicht ein versnobtes Beamtentum. Schlicht aber wirksam wäre die primäre Orientierung.

```html
<!DOCTYPE html>
<html lang="de">
<head>
<meta charset="utf-8">
<title>Lukas Brenner Veranstaltungstechnik – Fahrzeugbeschriftung</title>
<link rel="stylesheet" href="https://fonts.googleapis.com/css2?family=Montserrat:wght@500;600&family=PT+Sans+Narrow:wght@700&display=swap">
<style>
  :root {
    --page: #f8f8fb;
    --stage-top: #c9c9c9;
    --stage-bottom: #ffffff;
    --van-body: #fbfbfc;
    --van-line: #b9bcc0;
    --van-shade: #e4e6e9;
    --van-glass: #9fa3a8;
    --van-dark: #6b6e72;
    --van-tyre: #4a4c50;
    --van-rim: #c9cbcf;
    --van-light: #c9473f;
    --decor: #a7b1c8;
    --brand-navy: #2f4577;
    --brand-gray: #3d3d3f;
    --ground: #8a8a8a;
  }
  html, body {
    margin: 0;
    padding: 0;
    width: 1200px;
    height: 839px;
    overflow: hidden;
    background: var(--page);
  }
  .livery-sheet { display: block; width: 1200px; height: 839px; }

  .van-body { fill: var(--van-body); stroke: var(--van-line); stroke-width: 1.5; }
  .van-panel-line { fill: none; stroke: var(--van-line); stroke-width: 1.2; }
  .van-glass { fill: var(--van-glass); }
  .van-shade { fill: var(--van-shade); }
  .van-bumper { fill: var(--van-dark); }
  .van-tyre { fill: var(--van-tyre); }
  .van-rim { fill: var(--van-rim); stroke: #9a9da1; stroke-width: 1.5; }
  .van-lamp { fill: var(--van-light); }
  .van-handle { fill: none; stroke: var(--van-dark); stroke-width: 2; }
  .ground-line { stroke: var(--ground); stroke-width: 5; }
  .decor-field { fill: var(--decor); opacity: 0.75; }

  .brand-mark { fill: var(--brand-navy); }
  .brand-name {
    font-family: "Montserrat", sans-serif;
    font-weight: 600;
    fill: var(--brand-navy);
    letter-spacing: 0.12em;
  }
  .brand-descriptor {
    font-family: "Montserrat", sans-serif;
    font-weight: 500;
    fill: var(--brand-gray);
  }
  .contact-line {
    font-family: "PT Sans Narrow", sans-serif;
    font-weight: 700;
    fill: var(--brand-gray);
  }
  .claim {
    font-family: "PT Sans Narrow", sans-serif;
    font-weight: 700;
    fill: var(--brand-navy);
  }
  .door-detail {
    font-family: "Montserrat", sans-serif;
    font-weight: 500;
    fill: var(--brand-gray);
  }
</style>
</head>
<body>
<svg class="livery-sheet" viewBox="0 0 1200 839" xmlns="http://www.w3.org/2000/svg">
  <defs>
    <linearGradient id="stage-fade" x1="0" y1="0" x2="0" y2="1">
      <stop offset="0" stop-color="#c9c9c9"/>
      <stop offset="1" stop-color="#ffffff"/>
    </linearGradient>
    <clipPath id="side-body-clip">
      <path d="M74 700 L76 664 Q82 640 112 628 L178 604 L232 530 Q246 508 282 496 Q300 486 330 484 L748 484 Q768 486 772 504 L774 726 L74 726 Z"/>
    </clipPath>
    <clipPath id="rear-body-clip">
      <path d="M880 500 Q884 484 904 482 L1084 482 Q1104 484 1106 500 L1108 726 L878 726 Z"/>
    </clipPath>
  </defs>

  <rect class="stage-backdrop" x="42" y="21" width="1122" height="424" fill="url(#stage-fade)"/>
  <rect class="stage-floor" x="38" y="428" width="1126" height="395" fill="#ffffff"/>

  <!-- side view -->
  <g class="van-side" role="img" aria-label="Seitenansicht des weißen Kastenwagens">
    <path class="van-body" d="M74 700 L76 664 Q82 640 112 628 L178 604 L232 530 Q246 508 282 496 Q300 486 330 484 L748 484 Q768 486 772 504 L774 726 Q774 734 764 736 L700 736 Q690 690 652 690 Q614 690 606 736 L218 736 Q208 690 170 690 Q132 690 124 736 L84 736 Q74 730 74 700 Z"/>
    <path class="van-glass" d="M186 604 L232 548 Q240 538 256 536 L290 536 L290 604 Z"/>
    <path class="van-glass" d="M240 540 L256 498 L268 494 L252 538 Z" opacity="0.6"/>
    <path class="van-panel-line" d="M176 606 L176 700 Q186 712 200 714 L306 714 L306 498 M306 560 L772 560 M596 498 L596 714 M220 714 L600 714"/>
    <path class="van-handle" d="M290 632 L300 632"/>
    <rect class="van-glass" x="188" y="608" width="14" height="22" rx="4"/>
    <path class="van-shade" d="M90 650 Q104 640 126 636 L124 660 L86 664 Z"/>
    <path class="van-bumper" d="M74 688 L120 688 L120 720 L80 722 Q74 710 74 688 Z"/>
    <rect class="van-bumper" x="244" y="712" width="336" height="16" rx="2"/>
    <path class="van-bumper" d="M700 700 L774 700 L774 728 L704 728 Z"/>
    <rect class="van-lamp" x="760" y="606" width="14" height="58" rx="4"/>
    <circle class="van-tyre" cx="169" cy="733" r="41"/>
    <circle class="van-rim" cx="169" cy="733" r="22"/>
    <circle class="van-tyre" cx="653" cy="733" r="41"/>
    <circle class="van-rim" cx="653" cy="733" r="22"/>
  </g>

  <!-- rear view -->
  <g class="van-rear" role="img" aria-label="Heckansicht des weißen Kastenwagens">
    <rect class="van-body" x="836" y="582" width="22" height="46" rx="8"/>
    <rect class="van-body" x="1128" y="582" width="22" height="46" rx="8"/>
    <path class="van-body" d="M880 500 Q884 484 904 482 L1084 482 Q1104 484 1106 500 L1108 726 L878 726 Z"/>
    <rect class="van-lamp" x="966" y="484" width="50" height="7" rx="3"/>
    <rect class="van-lamp" x="866" y="600" width="20" height="70" rx="5"/>
    <rect class="van-lamp" x="1100" y="600" width="20" height="70" rx="5"/>
    <path class="van-panel-line" d="M993 490 L993 722"/>
    <rect x="904" y="664" width="76" height="14" fill="#ffffff" stroke="#6b6e72" stroke-width="1.5"/>
    <rect class="van-bumper" x="878" y="698" width="230" height="26"/>
    <rect class="van-tyre" x="868" y="724" width="28" height="48" rx="5"/>
    <rect class="van-tyre" x="1090" y="724" width="28" height="48" rx="5"/>
  </g>

  <line class="ground-line" x1="78" y1="778" x2="1132" y2="778"/>

  <!-- decorative field -->
  <rect class="decor-field" x="577" y="484" width="196" height="242" clip-path="url(#side-body-clip)" role="img" aria-label="Dekorfläche in Graublau"/>
  <rect class="decor-field" x="994" y="482" width="114" height="216" clip-path="url(#rear-body-clip)" role="img" aria-label="Dekorfläche in Graublau"/>

  <!-- side livery -->
  <circle class="brand-mark" cx="372" cy="556" r="56"/>
  <g transform="rotate(-4 497 555)">
    <text class="brand-name" x="497" y="555" font-size="29">LUKAS BRENNER</text>
    <text class="brand-descriptor" x="520" y="586" font-size="19">Veranstaltungstechnik</text>
  </g>
  <text class="contact-line" x="340" y="662" font-size="35" transform="rotate(-4 340 662)">www.lb-vt.de | +49 0151 238 4417</text>
  <text class="claim" x="341" y="694" font-size="17">Professioneller Full-Service-Partner</text>

  <!-- driver door -->
  <g class="livery-door">
    <circle class="brand-mark" cx="244" cy="646" r="7"/>
    <text class="brand-name" x="230" y="664" font-size="6.5" letter-spacing="0.05em">LUKAS BRENNER</text>
    <text class="door-detail" x="230" y="671" font-size="4.5">Veranstaltungstechnik</text>
    <text class="door-detail" x="230" y="678" font-size="3.6">Musterweg 12</text>
    <text class="door-detail" x="230" y="683" font-size="3.6">04109 Leipzig</text>
    <text class="door-detail" x="230" y="688" font-size="3.6">Telefon 0151 2384417</text>
    <text class="door-detail" x="230" y="693" font-size="3.6">info@lb-vt.de</text>
  </g>

  <!-- rear livery -->
  <circle class="brand-mark" cx="920" cy="558" r="26"/>
  <g transform="rotate(-4 952 563)">
    <text class="brand-name" x="952" y="563" font-size="15" letter-spacing="0.08em">LUKAS BRENNER</text>
    <text class="brand-descriptor" x="982" y="576" font-size="10">Veranstaltungstechnik</text>
  </g>
  <text class="contact-line" x="898" y="606" font-size="16" transform="rotate(-4 898 606)">www.lb-vt.de | +49 0151 238 4417</text>
  <text class="claim" x="902" y="697" font-size="12.5">Professioneller Full-Service-Partner</text>
</svg>
</body>
</html>
```